Corvane Alloys Collective Business Card

Design a business card for a new company. Corvane Alloys Collective is a subsidiary of KTP, Inc. (www.ktpreclaims.example)

Target Market(s)

B2B, Manufactures

Industry/Entity Type

Recycling

Contact Information for Business Card

Corvane Alloys Collective, LLC.
48217 North Wendlow Avenue
Alsip IL 60492
P: (312) 555-0143
F: (312) 555-0144
www.corvaneac.example
Email@corvaneac.example

Font styles to use
Sans Serif

Requirements
Must have
• A KTP, Inc. subsidiary company.
Nice to have
• Recycling Solutions. Uncompromised. (slogan)

```html
<!DOCTYPE html>
<html lang="en">
<head>
<meta charset="utf-8">
<title>Corvane Alloys Collective – Business Card</title>
<link rel="stylesheet" href="https://fonts.googleapis.com/css2?family=Source+Sans+3:wght@400;600&display=swap">
<style>
  :root {
    --bg-top: #2a2a2a;
    --bg-bottom: #050505;
    --card: #ffffff;
    --brand-green: #2f7d1e;
    --leaf-green: #5fa01f;
    --deep-green: #143f1c;
    --navy: #1d3473;
    --ink: #1b1b1b;
    --rule: #d9d9d9;
  }
  * { margin: 0; padding: 0; box-sizing: border-box; }
  html, body { width: 1200px; height: 900px; overflow: hidden; }
  body {
    background: linear-gradient(180deg, var(--bg-top) 0%, #151515 55%, var(--bg-bottom) 100%);
    font-family: "Source Sans 3", "Myriad Pro", Arial, sans-serif;
    position: relative;
  }
  .card {
    position: absolute;
    top: 306px;
    width: 440px;
    height: 271px;
    background: var(--card);
    border-radius: 12px;
  }
  .card--front { left: 149px; }
  .card--back { left: 608px; }

  .brand-name {
    position: absolute;
    color: var(--brand-green);
    font-weight: 600;
    text-align: center;
    line-height: 1.1;
  }
  .card--front .brand-name { left: 30px; top: 110px; width: 175px; font-size: 24px; }
  .card--back .brand-name { left: 90px; top: 88px; width: 260px; font-size: 30px; }

  .divider {
    position: absolute;
    left: 226px; top: 58px;
    width: 1px; height: 150px;
    background: linear-gradient(180deg, transparent, var(--rule) 20%, var(--rule) 80%, transparent);
  }
  .company {
    position: absolute; left: 247px; top: 52px;
    color: var(--leaf-green); font-size: 14.5px; font-weight: 600;
    white-space: nowrap;
  }
  .address {
    position: absolute; left: 247px; top: 74px;
    color: var(--ink); font-size: 12.5px; line-height: 19px;
  }
  .contacts {
    position: absolute; left: 247px; top: 131px;
    list-style: none; color: var(--ink); font-size: 12.5px;
  }
  .contacts li { display: flex; align-items: center; height: 18.3px; }
  .contacts svg { width: 10px; height: 10px; margin-right: 6px; fill: var(--leaf-green); }
  .slogan {
    position: absolute; left: 0; right: 0; top: 220px;
    text-align: center; font-size: 16.5px; font-weight: 600; color: var(--deep-green);
  }
  .slogan .accent { color: var(--navy); }

  .parent-note {
    position: absolute; left: 0; right: 0; top: 210px;
    text-align: center; color: var(--ink); font-size: 12.5px; line-height: 18px;
  }
</style>
</head>
<body>
  <section class="card card--front">
    <div class="brand-name">Corvane Alloys Collective</div>
    <div class="divider"></div>
    <p class="company">Corvane Alloys Collective, LLC.</p>
    <p class="address">48217 North Wendlow<br>Avenue Alsip IL 60492</p>
    <ul class="contacts">
      <li><svg viewBox="0 0 10 10"><path d="M2 0.5 L3.6 2.6 L2.7 3.6 Q3.6 5.6 6.4 7.3 L7.4 6.4 L9.5 8 L8.3 9.5 Q4 9 0.5 1.7 Z"/></svg>(312) 555-0143</li>
      <li><svg viewBox="0 0 10 10"><rect x="2.5" y="0.5" width="5" height="3"/><rect x="0.5" y="3.5" width="9" height="6" rx="1"/></svg>(312) 555-0144</li>
      <li><svg viewBox="0 0 10 10"><path d="M0.5 2 H9.5 V8.5 H0.5 Z M1 2.3 L5 5.5 L9 2.3" stroke="#fff" stroke-width="0.8"/></svg>Email@corvaneac.example</li>
      <li><svg viewBox="0 0 10 10"><path d="M3 7 L7 3" stroke="#5fa01f" stroke-width="1.4"/><rect x="0.8" y="5" width="4" height="2.6" rx="1.3" transform="rotate(-45 2.8 6.3)" fill="none" stroke="#5fa01f" stroke-width="1.2"/><rect x="5.2" y="2.4" width="4" height="2.6" rx="1.3" transform="rotate(-45 7.2 3.7)" fill="none" stroke="#5fa01f" stroke-width="1.2"/></svg>www.corvaneac.example</li>
    </ul>
    <p class="slogan">Recycling Solutions. <span class="accent">Uncompromised</span></p>
  </section>

  <section class="card card--back">
    <div class="brand-name">Corvane Alloys Collective</div>
    <p class="parent-note">Corvane Alloys Collective is a subsidiary of KTP, Inc.<br>www.ktpreclaims.example</p>
  </section>
</body>
</html>
```